Event Program Design

We are looking to create a stunning event program for “Velvet Gala Night,” presented by The Marlow Chamber Society. This program will reflect the upscale theme of the event while maintaining a clean, elegant layout. We will use a past year’s program as a reference to replicate a similar structure and overall flow, including all page layouts. The cover design will incorporate both front and back, with an inside cover that carries through the sophisticated look established on the front.
Because there are 31 individuals to feature, along with group photos, the program will require enough pages to accommodate everyone without feeling overcrowded (use previous design for reference).
We also have inspirational images and the event invitation available for reference. Please note that these images are for layout purposes only and should not be used for any design elements in the new design—they are solely meant to inspire the final product’s style and color palette.
We plan to base the program’s color scheme on the invitation’s aesthetic; however, we want to avoid directly copying any design features from the reference images or the previous year’s sample. Font selections should complement the elegant theme and must be free to download and use commercially.
The new design should set up for 8 x 11 print size, full color. Please include adequate bleed for print. Will be using prentora for printing so please contact them for any additional questions.
Our goal is a cohesive, refined program that helps attendees navigate the evening’s events while reflecting the grandeur of The Marlow Chamber Society’s “Velvet Gala Night.” We look forward to a layout that strikes the perfect balance between classic sophistication and modern flair—something as memorable as the event itself.

```html
<!DOCTYPE html>
<html lang="en">
<head>
<meta charset="utf-8">
<title>Velvet Gala Night — Event Program</title>
<link rel="stylesheet" href="https://fonts.googleapis.com/css2?family=Playfair+Display:wght@400;500;600&family=Montserrat:wght@400;500;600&display=swap">
<style>
:root{
  --canvas:#e8e8ea;
  --ink:#141414;
  --night:#0c0c0d;
  --paper:#ffffff;
  --paper-tint:#f4f3f4;
  --gold:#c8a152;
  --blush:#f2b3bb;
  --blush-deep:#e48a98;
  --wine:#8d1a2c;
  --wine-dark:#5e0f1c;
  --silver:#bfc1c6;
  --muted:#5b5b5b;
}
*{margin:0;padding:0;box-sizing:border-box}
html,body{width:1200px;height:3000px;overflow:hidden}
body{background:var(--canvas);position:relative;font-family:"Montserrat",sans-serif;color:var(--ink)}
.page{position:absolute;width:470px;height:646px;overflow:hidden;background:var(--paper);box-shadow:0 2px 6px rgba(0,0,0,.12)}
.page--dark{background:var(--night);color:#fff}
.page--light{background:linear-gradient(180deg,var(--paper) 0%,var(--paper-tint) 100%)}
.frame{position:absolute;border:1.5px solid var(--gold)}
.bloom{position:absolute;border-radius:50%}
.bloom--blush{background:radial-gradient(circle at 50% 50%,#fbe3e6 0%,var(--blush) 45%,var(--blush-deep) 100%)}
.bloom--wine{background:radial-gradient(circle at 50% 50%,#c23a4f 0%,var(--wine) 50%,var(--wine-dark) 100%)}
.disco{position:absolute;border-radius:50%;background:radial-gradient(circle at 35% 35%,#ffffff 0%,var(--silver) 45%,#6f7178 100%)}
.center{position:absolute;left:0;right:0;text-align:center}
.kicker{font-size:10px;letter-spacing:2.4px;text-transform:uppercase;font-weight:500;line-height:1.6}
.title{font-family:"Playfair Display",serif;font-weight:400;line-height:.95}
.title .accent{color:var(--blush-deep)}
.title .accent-wine{color:var(--wine)}
.year{font-family:"Playfair Display",serif;letter-spacing:8px}
.small{font-size:8.5px;line-height:1.5;color:var(--muted)}
.red{color:var(--wine)}
.names{position:absolute;font-size:8.5px;line-height:2.05;list-style:none}
.names li::before{content:"";display:inline-block;width:4px;height:4px;border-radius:50%;background:var(--wine);margin-right:6px;vertical-align:middle}
.society{font-family:"Playfair Display",serif;font-size:12px;color:var(--muted)}
.photo{position:absolute;border-radius:4px}
.tickets{position:absolute;font-size:8px;line-height:2.2;list-style:none}
.tickets .price{display:inline-block;background:var(--wine);color:#fff;padding:0 4px;margin-right:6px;line-height:1.5;font-weight:600}
.form-line{position:absolute;height:1px;background:#9a9a9a}
.label{position:absolute;font-size:8px;color:var(--muted)}
</style>
</head>
<body>

<!-- Front cover -->
<section class="page page--dark" style="left:104px;top:24px">
  <div class="frame" style="left:92px;top:40px;width:286px;height:566px;border-radius:143px 143px 143px 143px/150px 150px 150px 150px"></div>
  <div class="photo" role="img" aria-label="Photo of a glittering disco ball" style="left:170px;top:78px;width:130px;height:130px;border-radius:50%;background:radial-gradient(circle at 40% 40%,#e9e9ea 0%,#8a8b90 55%,#2a2a2c 100%)"></div>
  <p class="center kicker" style="top:250px">You are cordially<br>invited to attend a</p>
  <h1 class="center title" style="top:300px;font-size:58px">Velvet Gala<br><span class="accent">Night</span></h1>
  <p class="center year" style="top:430px;font-size:22px">2025</p>
  <div class="bloom bloom--blush" role="img" aria-label="Blush dahlia cluster" style="left:300px;top:10px;width:120px;height:120px"></div>
  <div class="bloom bloom--blush" role="img" aria-label="Blush dahlia" style="left:370px;top:90px;width:90px;height:90px"></div>
  <div class="bloom bloom--wine" role="img" aria-label="Deep red dahlia" style="left:330px;top:470px;width:130px;height:130px"></div>
  <div class="bloom bloom--blush" role="img" aria-label="Blush dahlia" style="left:250px;top:510px;width:100px;height:100px"></div>
  <div class="bloom bloom--blush" role="img" aria-label="Blush dahlia" style="left:40px;top:540px;width:90px;height:90px"></div>
</section>

<!-- Back cover -->
<section class="page page--dark" style="left:628px;top:24px">
  <div class="frame" style="left:30px;top:30px;width:410px;height:586px"></div>
  <div class="bloom bloom--blush" role="img" aria-label="Blush dahlia cluster" style="left:-20px;top:-20px;width:130px;height:130px"></div>
  <div class="bloom bloom--blush" role="img" aria-label="Blush dahlia" style="left:90px;top:10px;width:70px;height:70px"></div>
  <div class="bloom bloom--blush" role="img" aria-label="Small blush flower spray" style="left:205px;top:210px;width:60px;height:45px"></div>
  <h2 class="center title" style="top:265px;font-size:46px">Velvet Gala <span class="accent">Night</span></h2>
  <p class="center year" style="top:325px;font-size:20px">2025</p>
  <div class="bloom bloom--wine" role="img" aria-label="Red dahlia cluster" style="left:170px;top:370px;width:80px;height:80px"></div>
  <div class="bloom bloom--blush" role="img" aria-label="Blush dahlia" style="left:230px;top:375px;width:70px;height:70px"></div>
  <div class="disco" role="img" aria-label="Disco ball" style="left:380px;top:550px;width:80px;height:80px"></div>
</section>

<!-- Invitation page -->
<section class="page page--light" style="left:104px;top:744px">
  <div class="frame" style="left:30px;top:30px;width:410px;height:586px"></div>
  <div class="bloom bloom--wine" role="img" aria-label="Deep red dahlia" style="left:-20px;top:-20px;width:110px;height:110px"></div>
  <div class="bloom bloom--blush" role="img" aria-label="Blush dahlia" style="left:60px;top:-10px;width:70px;height:70px"></div>
  <p class="center kicker" style="top:60px">You are cordially<br>invited to attend a</p>
  <h2 class="center title" style="top:100px;font-size:54px">Velvet Gala<br><span class="accent-wine">Night</span></h2>
  <p class="center small" style="top:225px;padding:0 120px">Benefiting the Harrow Valley Symphony and Friends of the Cedar Basin, honoring the 2025 Belles and Beaux</p>
  <p class="center red" style="top:280px;font-family:'Playfair Display',serif;font-size:17px">8<sup style="font-size:9px">TH</sup> February, Saturday</p>
  <p class="center" style="top:312px"><span style="background:var(--wine);color:#fff;font-size:9px;font-weight:600;padding:3px 8px;letter-spacing:1px">7:00 PM</span> <span style="font-size:9px;letter-spacing:1px">TO MIDNIGHT</span></p>
  <p class="center small" style="top:345px;color:var(--ink)">Lindenhall Hotel &amp; Conference Center<br>420 Larkspur Avenue, Marlow</p>
  <p class="center small" style="top:385px">Black Tie Optional<br>Dinner and Dancing to Follow</p>
  <div class="disco" role="img" aria-label="Disco ball" style="left:60px;top:510px;width:70px;height:70px"></div>
  <div class="bloom bloom--blush" role="img" aria-label="Blush dahlia cluster" style="left:200px;top:500px;width:120px;height:120px"></div>
  <div class="bloom bloom--wine" role="img" aria-label="Deep red dahlia" style="left:320px;top:470px;width:140px;height:140px"></div>
  <div class="bloom bloom--blush" role="img" aria-label="Blush dahlia" style="left:130px;top:560px;width:90px;height:90px"></div>
</section>

<!-- Senior Belles -->
<section class="page page--light" style="left:628px;top:744px">
  <div class="frame" style="left:30px;top:30px;width:410px;height:586px"></div>
  <div class="disco" role="img" aria-label="Disco balls" style="left:40px;top:10px;width:50px;height:50px"></div>
  <div class="bloom bloom--blush" role="img" aria-label="Blush dahlia" style="left:390px;top:-10px;width:90px;height:90px"></div>
  <p class="center society" style="top:55px">— The Marlow Chamber Society —</p>
  <h2 class="center title" style="top:80px;font-size:44px"><span class="accent-wine">Senior</span><br>Belles</h2>
  <ul class="names" style="left:62px;top:190px">
    <li>Ava Kendall</li><li>Brooke Hollis</li><li>Camila Reyes</li><li>Delia Marsh</li><li>Elise Warren</li><li>Faith Collier</li><li>Grace Whitley</li><li>Harper Lane</li><li>Iris Pennington</li><li>Julia Stroud</li><li>Kate Ambrose</li><li>Lila Harding</li>
  </ul>
  <ul class="names" style="left:250px;top:190px">
    <li>Madeline Frost</li><li>Nora Castillo</li><li>Olivia Brandt</li><li>Paige Holloway</li><li>Quinn Ellery</li><li>Rosa Delgado</li><li>Sadie Whitmore</li><li>Tessa Lowell</li><li>Vera Ashby</li><li>Willa Sutton</li><li>Yara Fielding</li><li>Zoe Carrington</li>
  </ul>
  <div class="bloom bloom--blush" role="img" aria-label="Blush dahlia cluster" style="left:20px;top:520px;width:110px;height:110px"></div>
  <div class="bloom bloom--wine" role="img" aria-label="Deep red dahlia" style="left:180px;top:510px;width:130px;height:130px"></div>
  <div class="bloom bloom--blush" role="img" aria-label="Blush dahlia" style="left:340px;top:530px;width:120px;height:120px"></div>
</section>

<!-- Senior Beaux -->
<section class="page page--light" style="left:104px;top:1484px">
  <div class="frame" style="left:30px;top:30px;width:410px;height:586px"></div>
  <div class="disco" role="img" aria-label="Disco balls" style="left:20px;top:10px;width:60px;height:60px"></div>
  <div class="bloom bloom--blush" role="img" aria-label="Blush dahlia" style="left:-20px;top:-20px;width:70px;height:70px"></div>
  <p class="center society" style="top:65px">— The Marlow Chamber Society —</p>
  <h2 class="center title" style="top:92px;font-size:44px"><span class="accent-wine">Senior</span><br>Beaux</h2>
  <ul class="center" style="top:205px;list-style:none;font-size:9px;line-height:2.1">
    <li>Caleb Ashford</li><li>Dylan Mercer</li><li>Ethan Rowland</li><li>Gavin Sterling</li><li>Luke Brennan</li><li>Miles Thornton</li><li>Owen Caldwell</li>
  </ul>
  <div class="bloom bloom--blush" role="img" aria-label="Blush dahlia cluster" style="left:20px;top:450px;width:130px;height:130px"></div>
  <div class="bloom bloom--wine" role="img" aria-label="Deep red dahlia" style="left:150px;top:470px;width:150px;height:150px"></div>
  <div class="bloom bloom--blush" role="img" aria-label="Blush dahlia" style="left:60px;top:560px;width:100px;height:100px"></div>
</section>

<!-- Tickets & payment -->
<section class="page page--light" style="left:628px;top:1484px">
  <div class="frame" style="left:30px;top:30px;width:410px;height:586px"></div>
  <div class="bloom bloom--wine" role="img" aria-label="Deep red dahlia" style="left:20px;top:-20px;width:90px;height:90px"></div>
  <div class="disco" role="img" aria-label="Disco ball" style="left:340px;top:-10px;width:60px;height:60px"></div>
  <div class="bloom bloom--blush" role="img" aria-label="Blush dahlia" style="left:390px;top:-15px;width:80px;height:80px"></div>
  <h2 class="center title" style="top:75px;font-size:40px">Velvet Gala<br><span class="accent-wine">Night</span></h2>
  <ul class="tickets" style="left:70px;top:175px">
    <li><span class="price">$2,500</span>Platinum Table</li><li><span class="price">$1,500</span>Gold Table</li><li><span class="price">$1,000</span>Silver Table</li><li><span class="price">$750</span>Bronze Table</li>
  </ul>
  <ul class="tickets" style="left:250px;top:175px">
    <li><span class="price">$300</span>Couple Ticket</li><li><span class="price">$150</span>Single Ticket</li><li><span class="price">$75</span>Student Ticket</li><li><span class="price">$50</span>Sponsor Gift</li>
  </ul>
  <p class="center" style="top:275px;font-family:'Playfair Display',serif;font-size:14px">Payment Information</p>
  <div class="form-line" style="left:60px;top:298px;width:350px"></div>
  <p class="small" style="position:absolute;left:60px;top:310px;width:160px">Make checks payable to the Marlow Chamber Society.</p>
  <p class="small" style="position:absolute;left:250px;top:310px;width:160px">I am unable to attend, but please accept my gift.</p>
  <p class="label" style="left:60px;top:350px">Please charge my:</p>
  <p class="label" style="left:60px;top:375px">Card #</p><div class="form-line" style="left:95px;top:386px;width:125px"></div>
  <p class="label" style="left:250px;top:375px">Exp.</p><div class="form-line" style="left:275px;top:386px;width:135px"></div>
  <p class="label" style="left:60px;top:400px">Name</p><div class="form-line" style="left:95px;top:411px;width:125px"></div>
  <p class="label" style="left:250px;top:400px">Signature</p><div class="form-line" style="left:295px;top:411px;width:115px"></div>
  <p class="center small" style="top:440px">Mail to: P.O. Box 1180, Marlow</p>
  <div class="bloom bloom--wine" role="img" aria-label="Deep red dahlia" style="left:140px;top:520px;width:110px;height:110px"></div>
  <div class="bloom bloom--blush" role="img" aria-label="Blush dahlia cluster" style="left:240px;top:530px;width:110px;height:110px"></div>
  <div class="bloom bloom--blush" role="img" aria-label="Blush dahlia" style="left:340px;top:560px;width:80px;height:80px"></div>
</section>

<!-- Photo page -->
<section class="page page--light" style="left:365px;top:2224px">
  <div class="frame" style="left:30px;top:30px;width:410px;height:586px"></div>
  <div class="bloom bloom--blush" role="img" aria-label="Blush dahlia cluster" style="left:330px;top:-20px;width:130px;height:130px"></div>
  <div class="bloom bloom--wine" role="img" aria-label="Deep red dahlia" style="left:290px;top:40px;width:80px;height:80px"></div>
  <div class="photo" role="img" aria-label="Group photo of the honorees" style="left:75px;top:140px;width:150px;height:150px;background:linear-gradient(135deg,#6f8a72,#c9c2b4)"></div>
  <div class="photo" role="img" aria-label="Event photo of glassware" style="left:245px;top:140px;width:150px;height:150px;background:linear-gradient(135deg,#3a3432,#b8a79a)"></div>
  <div class="photo" role="img" aria-label="Photo of disco balls" style="left:75px;top:310px;width:150px;height:150px;background:linear-gradient(135deg,#b7c4d6,#d9a6c0)"></div>
  <div class="photo" role="img" aria-label="Photo of champagne toast" style="left:245px;top:310px;width:150px;height:150px;background:linear-gradient(135deg,#4a4340,#d4c6b2)"></div>
  <div class="bloom bloom--blush" role="img" aria-label="Blush dahlia cluster" style="left:-10px;top:490px;width:130px;height:130px"></div>
  <div class="bloom bloom--wine" role="img" aria-label="Deep red dahlia" style="left:90px;top:540px;width:110px;height:110px"></div>
</section>

</body>
</html>
```